NEW! Sports Supplement label
Vital Kinetic Laboratories
Project: NEW! Sports Supplement label
NEW! Sports Supplement label - Sports
Creative Brief
Looking for a new packaging design for a new line of products. This needs to be a clean label that delivers a scientific or medical feel in 3 colors with 4 lines for product descriptor sublines. <p><p> For Example: <p> • Muscle Recovery Acceleration <p> • Nitric Oxide Production <p> • Maximum Muscle Mass <p> • Improved Energy &amp; Focus <p><p> Use the following elements for presentation: <p><p> Name: VK260Q <p><p> 120 Capsules Dietary Supplement <p><p> The products are geared to Sports Supplements, Fat burners, preworkout supplements, sport drinks. <p><p> The fonts for the Product name and VKL logo must be destinctive elements and pop that adds value by providing consumers with instantly recognizable cues to help with the purchase decision making process. Preferrably reversed out white or black. <p> <p> Please see the following sites as example product labels for creative thought. They also provide actual full labels for your review: <p><p> http://www.plorvex.com/product/index.jsp?productId=48573920 http://www.plorvex.com/product/index.jsp?productId=48619375 http://www.plorvex.com/product/index.jsp?productId=48926054 <p><p> The label should be clean, in that it provides a clear, attractive space, with key information (4 line product descriptor mentioned above) on the front display panel necessary for a consumer to make a quick purchase decision. <p> The label should communicate a concise but informative message designed to make the consumer feel comfortable with the product by providing consumers with instantly recognizable cues (symbols of quality) to help with the purchase decision making process.
Sports
Sports nutrition products target a mass audience of consumers who have grown up knowing an active lifestyle has positive, long-term implications for health, fitness, weight management and longevity.
Please provide label design with color codes and in standard file formats with element layers. 2.75 x 7.00 4 x 9.375

```html
<!DOCTYPE html>
<html lang="en">
<head>
<meta charset="utf-8">
<title>VK260Q Dietary Supplement Label</title>
<link href="https://fonts.googleapis.com/css2?family=Archivo+Black&family=Roboto:wght@500;700;900&family=Roboto+Condensed:wght@700&display=swap" rel="stylesheet">
<style>
  :root {
    --blue-deep: #0d3f7e;
    --blue-mid: #1f63ad;
    --blue-light: #3d86cf;
    --navy-text: #1c4d8a;
    --silver-light: #f4f5f7;
    --silver-mid: #b9bec6;
    --silver-dark: #5f666f;
    --white: #ffffff;
    --black: #0b0b0b;
  }
  * { margin: 0; padding: 0; box-sizing: border-box; }
  html, body { width: 1200px; height: 929px; overflow: hidden; background: #fff; }
  .label {
    position: relative;
    width: 1200px;
    height: 929px;
    overflow: hidden;
    background:
      repeating-linear-gradient(90deg, rgba(255,255,255,0.05) 0 14px, rgba(0,0,0,0.04) 14px 40px, rgba(255,255,255,0.03) 40px 58px),
      linear-gradient(90deg, var(--blue-deep) 0%, var(--blue-mid) 30%, var(--blue-light) 50%, var(--blue-mid) 70%, var(--blue-deep) 100%);
  }
  .metal-band {
    position: absolute; left: 0; width: 100%;
    background: linear-gradient(180deg, var(--silver-mid) 0%, var(--silver-light) 35%, var(--silver-dark) 55%, var(--silver-light) 80%, var(--silver-mid) 100%);
  }
  .metal-band--top { top: 0; height: 45px; }
  .metal-band--bottom { bottom: 0; height: 40px; }
  .brand {
    position: absolute; top: 58px; left: 0; width: 100%;
    text-align: center; color: var(--white);
    font-family: "Roboto", Arial, sans-serif;
  }
  .brand__mark { font-size: 92px; font-weight: 900; line-height: 1; letter-spacing: 1px; }
  .brand__name { margin-top: 10px; font-size: 31px; font-weight: 700; letter-spacing: 1px; }
  .product-name {
    position: absolute; top: 245px; left: 0; width: 100%;
    text-align: center;
    font-family: "Archivo Black", "Arial Black", sans-serif;
    font-size: 235px; line-height: 1; letter-spacing: 2px;
    transform: scaleX(0.82);
    background: linear-gradient(180deg, #ffffff 0%, #e9ecef 35%, #8d949c 52%, #d9dde1 70%, #f7f8f9 100%);
    -webkit-background-clip: text; background-clip: text;
    color: transparent;
    -webkit-text-stroke: 2px #2a2f36;
    filter: drop-shadow(4px 6px 4px rgba(0,0,0,0.45));
  }
  .descriptor {
    position: absolute; top: 452px; right: 158px;
    font-family: "Roboto", Arial, sans-serif; font-weight: 700;
    font-size: 60px; line-height: 1; color: var(--white); letter-spacing: 1px;
    text-shadow: 2px 3px 4px rgba(0,0,0,0.3);
  }
  .benefits-panel {
    position: absolute; left: 115px; top: 547px; width: 970px; height: 360px;
    border-radius: 30px 30px 0 0;
    background: linear-gradient(180deg, #ffffff 0%, #f3f4f6 60%, #dfe2e6 100%);
    box-shadow: 0 -3px 10px rgba(0,0,0,0.25);
  }
  .benefits {
    list-style: none; position: absolute; left: 43px; top: 55px;
    font-family: "Roboto Condensed", Arial, sans-serif; font-weight: 700;
    font-size: 37px; color: var(--navy-text); line-height: 47px;
  }
  .benefits li { display: flex; align-items: center; }
  .benefits svg { width: 20px; height: 20px; margin-right: 18px; flex: none; }
  .count-badge {
    position: absolute; left: 883px; top: 750px; width: 160px; height: 145px;
    background: var(--black); border-radius: 18px 18px 0 0;
    color: var(--white); text-align: center;
    font-family: "Roboto", Arial, sans-serif;
  }
  .count-badge__number { font-size: 82px; font-weight: 700; line-height: 1; margin-top: 14px; }
  .count-badge__unit { font-size: 22px; font-weight: 700; letter-spacing: 0.5px; margin-top: 4px; }
</style>
</head>
<body>
  <main class="label">
    <div class="metal-band metal-band--top"></div>

    <header class="brand">
      <div class="brand__mark">VKL</div>
      <div class="brand__name">VITAL KINETIC LABORATORIES</div>
    </header>

    <h1 class="product-name">VK260Q</h1>
    <div class="descriptor">DIETARY SUPPLEMENT</div>

    <section class="benefits-panel">
      <ul class="benefits">
        <li><svg viewBox="0 0 10 10"><path d="M1 1 L9 5 L1 9 L3 5 Z" fill="#222"/></svg>Muscle Recovery Acceleration</li>
        <li><svg viewBox="0 0 10 10"><path d="M1 1 L9 5 L1 9 L3 5 Z" fill="#222"/></svg>NItric Oxide Production</li>
        <li><svg viewBox="0 0 10 10"><path d="M1 1 L9 5 L1 9 L3 5 Z" fill="#222"/></svg>Maximum Musle Mass</li>
        <li><svg viewBox="0 0 10 10"><path d="M1 1 L9 5 L1 9 L3 5 Z" fill="#222"/></svg>Improved Energy &amp; Focus</li>
      </ul>
    </section>

    <div class="count-badge">
      <div class="count-badge__number">30</div>
      <div class="count-badge__unit">CAPSULES</div>
    </div>

    <div class="metal-band metal-band--bottom"></div>
  </main>
</body>
</html>
```